Floristry Business Card Design Project

I have a logo now and am looking to incorporate this into a business card. I would like a double sided business card. I would like one side to be decorative so that it blends well when included with floral arrangements and that can also be used as the front of a card and the other side will contain the business details. The font on the business details side should be clear although some decorative font would be ok. I have included the logo files for use in the business card design.

Feel free to break up the logo and use certain aspects of it in the design. Really looking for something that stands out and that is really creative.

Industry/Entity Type

Floral

Requirements
Should not have
• Nothing tacky or corny. The logo should be clearly read (perhaps a background colour).

```html
<!DOCTYPE html>
<html lang="en">
<head>
<meta charset="utf-8">
<title>Petal Hollow – Business Card</title>
<link rel="stylesheet" href="https://fonts.googleapis.com/css2?family=PT+Sans:wght@400;700&display=swap">
<style>
  :root {
    --backdrop: #e9e9e9;
    --card: #ffffff;
    --sage: #7dbd9c;
    --coral: #e9846c;
    --ink: #3e3e3e;
    --divider: #c9c9c9;
  }
  * { margin: 0; padding: 0; box-sizing: border-box; }
  html, body { width: 1200px; height: 974px; overflow: hidden; }
  body {
    background: var(--backdrop);
    font-family: "PT Sans", sans-serif;
    color: var(--ink);
    position: relative;
  }
  .card {
    position: absolute;
    left: 280px;
    width: 640px;
    height: 366px;
    background: var(--card);
    border-radius: 26px;
    box-shadow: 0 6px 22px rgba(0,0,0,0.12);
  }
  .card--front { top: 70px; }
  .card--back { top: 520px; display: flex; }

  /* Front */
  .front-mark {
    position: absolute;
    top: 70px; left: 0; right: 0;
    display: flex; flex-direction: column; align-items: center; gap: 20px;
  }
  .front-mark .dot {
    width: 120px; height: 120px; border-radius: 50%;
    border: 2px solid var(--sage);
  }
  .brand-name {
    font-weight: 400;
    color: var(--sage);
    letter-spacing: 0.3em;
    text-transform: uppercase;
    font-size: 20px;
  }
  .front-url {
    position: absolute;
    left: 0; right: 0; bottom: 46px;
    text-align: center;
    font-size: 20px;
    letter-spacing: 0.32em;
    color: var(--ink);
  }

  /* Back */
  .back-brand {
    width: 50%;
    display: flex; flex-direction: column; align-items: center; justify-content: center; gap: 22px;
  }
  .back-brand .dot {
    width: 130px; height: 130px; border-radius: 50%;
    border: 2px solid var(--sage);
  }
  .back-divider {
    width: 1px; margin: 46px 0;
    background: linear-gradient(var(--backdrop), var(--divider), var(--backdrop));
  }
  .contact {
    flex: 1;
    padding: 58px 0 0 34px;
  }
  .contact__name { font-size: 24px; font-weight: 700; color: var(--sage); line-height: 1.1; }
  .contact__title { font-size: 16px; color: var(--coral); margin-bottom: 10px; }
  .contact__list { list-style: none; }
  .contact__list li {
    display: flex; align-items: center; gap: 10px;
    font-size: 17px; line-height: 28px;
  }
  .contact__list svg { width: 16px; height: 16px; flex: none; }
  .contact__address { font-size: 17px; line-height: 24px; margin-top: 4px; }
</style>
</head>
<body>

<section class="card card--front" aria-label="Card front">
  <div class="front-mark">
    <span class="dot"></span>
    <span class="brand-name">Petal Hollow</span>
  </div>
  <p class="front-url">www.petalhollow.com</p>
</section>

<section class="card card--back" aria-label="Card back">
  <div class="back-brand">
    <span class="dot"></span>
    <span class="brand-name">Petal Hollow</span>
  </div>
  <div class="back-divider"></div>
  <div class="contact">
    <p class="contact__name">Your Name</p>
    <p class="contact__title">Title</p>
    <ul class="contact__list">
      <li>
        <svg viewBox="0 0 16 16" aria-hidden="true"><circle cx="8" cy="8" r="7" fill="none" stroke="#e9846c" stroke-width="1.4"/><path d="M5.5 4.5l1.5 1.5-1 1c.6 1.2 1.5 2.1 2.8 2.8l1-1 1.5 1.5-1 1.2C7.6 11 5 8.4 4.5 5.6z" fill="#e9846c"/></svg>
        012-345-6789
      </li>
      <li>
        <svg viewBox="0 0 16 16" aria-hidden="true"><rect x="4.5" y="1.5" width="7" height="13" rx="1.4" fill="none" stroke="#e9846c" stroke-width="1.4"/><circle cx="8" cy="12" r="0.9" fill="#e9846c"/></svg>
        012-345-6789
      </li>
      <li>
        <svg viewBox="0 0 16 16" aria-hidden="true"><rect x="1.5" y="3.5" width="13" height="9" rx="1" fill="none" stroke="#e9846c" stroke-width="1.4"/><path d="M1.5 4l6.5 5 6.5-5" fill="none" stroke="#e9846c" stroke-width="1.4"/></svg>
        admin@petalhollow.com
      </li>
      <li>
        <svg viewBox="0 0 16 16" aria-hidden="true"><circle cx="8" cy="8" r="6.5" fill="none" stroke="#e9846c" stroke-width="1.4"/><ellipse cx="8" cy="8" rx="2.8" ry="6.5" fill="none" stroke="#e9846c" stroke-width="1.2"/><path d="M1.5 8h13" stroke="#e9846c" stroke-width="1.2"/></svg>
        www.petalhollow.com
      </li>
    </ul>
    <p class="contact__address">Street Name, City Name<br>Zip Code-00000</p>
  </div>
</section>

</body>
</html>
```